Wordpress website for voluntary transgender support online

We need a website as an information support for transgender people and their friends and families. We are a self funded voluntary support group reaching out to educate all in need.
Fairly basic site. Tabs for 3 of us to put bios, professional resources and contacts, news, general information, our contact info, entertainment.
Our logo is attached and we'd love the use of clouds and the colour lilac. We wish to look professional but approachable and personable.

Target Market(s)

Transgender people,mr heir families and friends and general public.

Industry/Entity Type

Group

Requirements
Must have
• Willow 4 logo.
• Tabs for: about us, contacts, news, bios x3, suggestions, professional resources, entertainment, personal resources, general information.
• We are hoping to set up in Wordpress so that we can then manage the page and update in the future.
• Coding will be required.
Nice to have
• Any suggestions.

```html
<!DOCTYPE html>
<html lang="en">
<head>
<meta charset="utf-8">
<title>Willow 4 – Transgender Support</title>
<link href="https://fonts.googleapis.com/css2?family=Open+Sans:wght@300;400;600;700&family=Great+Vibes&display=swap" rel="stylesheet">
<style>
:root{
  --lilac:#b9a6dc;
  --lilac-pale:#efe9f8;
  --purple:#6a4a9c;
  --purple-deep:#4f3480;
  --ink:#3d3d4a;
  --muted:#6f6f7c;
  --white:#ffffff;
  --rule:#d9d0ea;
}
*{box-sizing:border-box;margin:0;padding:0}
html,body{width:1200px;height:2276px;overflow:hidden}
body{font-family:"Open Sans",Arial,sans-serif;color:var(--ink);
  background:linear-gradient(180deg,#f6f2fc 0%,#ece4f7 35%,#f3eefa 60%,#e6dcf4 100%);position:relative}
.hero{position:absolute;left:0;top:0;width:1200px;height:800px;
  background:radial-gradient(ellipse at 30% 30%,#fbf7ff 0%,#e4d8f4 40%,#c8b5e6 75%,#b19ad8 100%)}
.header{position:absolute;left:0;top:0;width:1200px;height:140px}
.logo{position:absolute;left:90px;top:50px;display:flex;align-items:center;gap:12px}
.logo-dot{width:26px;height:26px;border-radius:50%;background:var(--purple)}
.logo-name{font-size:44px;font-weight:600;color:var(--purple)}
.nav{position:absolute;right:90px;top:76px;display:flex;gap:6px}
.nav a{font-size:15px;color:var(--ink);text-decoration:none;padding:8px 14px;border-radius:4px}
.nav a.active{background:var(--white);border:1px solid var(--rule)}
.tagline{position:absolute;left:720px;top:430px;width:380px;text-align:center;
  font-family:"Great Vibes",cursive;font-size:46px;line-height:1.05;color:var(--purple-deep)}
.wave{position:absolute;left:0;top:640px;width:1200px;height:180px}
.section-title{position:absolute;left:0;width:1200px;text-align:center;font-size:40px;font-weight:300;color:var(--ink)}
.intro{position:absolute;left:180px;width:840px;text-align:center;font-size:13px;line-height:1.65;color:var(--muted)}
.intro strong{color:var(--ink);font-weight:600}
.rule{position:absolute;left:136px;width:928px;height:1px;background:var(--rule)}
.mission{position:absolute;left:136px;top:1100px;width:928px;display:flex;justify-content:space-between}
.mission-item{width:170px;text-align:center;font-size:12px;line-height:1.5;color:var(--muted)}
.mission-item svg{display:block;margin:0 auto 12px}
.news{position:absolute;left:136px;top:1340px;width:928px;display:flex;gap:12px}
.news-card{width:223px}
.news-photo{height:200px;border-radius:2px}
.news-title{font-size:12px;color:var(--purple);margin-top:10px}
.news-date{font-size:11px;color:var(--muted);margin-top:4px}
.arrow{position:absolute;top:1460px;font-size:30px;color:var(--lilac)}
.testimonial{position:absolute;left:136px;top:1660px;width:928px;height:240px;background:var(--white);display:flex}
.quote-body{flex:1;padding:36px 40px;position:relative}
.quote-mark{font-size:60px;color:var(--purple);line-height:.5;font-family:Georgia,serif}
.quote-text{font-size:13px;line-height:1.7;color:var(--muted);margin:-8px 0 0 46px}
.quote-name{font-size:18px;color:var(--purple);margin:18px 0 0 46px}
.quote-photo{width:320px;height:240px;background:linear-gradient(135deg,#e9e2ee,#b7a49a 60%,#6d5548)}
.dots{position:absolute;left:170px;top:1870px;display:flex;gap:8px}
.dots span{width:12px;height:12px;border-radius:50%;background:var(--rule)}
.dots span.on{background:var(--purple)}
.contact-line{position:absolute;left:0;top:2130px;width:1200px;display:flex;justify-content:center;gap:40px;font-size:14px;color:var(--ink)}
.contact-line span{display:flex;align-items:center;gap:8px}
.footer{position:absolute;left:0;top:2180px;width:1200px;height:96px;background:var(--purple);color:var(--white)}
.footer-links{position:absolute;left:40px;top:28px;font-size:13px}
.footer-copy{position:absolute;left:40px;top:54px;font-size:12px;opacity:.8}
.social{position:absolute;right:40px;top:26px;display:flex;gap:10px}
.social span{width:40px;height:40px;border-radius:50%;background:#8f74bd}
</style>
</head>
<body>
<div class="hero" role="img" aria-label="Soft lilac sky of clouds with a sunlit glow"></div>

<header class="header">
  <div class="logo"><span class="logo-dot"></span><span class="logo-name">Willow 4</span></div>
  <nav class="nav">
    <a class="active">Home</a><a>About us</a><a>Bios</a><a>News</a><a>Suggestions</a><a>Resources</a><a>Contact us</a>
  </nav>
</header>

<p class="tagline">Phasellus nisl est condimentum vitae faucibus</p>

<svg class="wave" viewBox="0 0 1200 180" preserveAspectRatio="none">
  <path d="M0 120 C300 20 700 10 1200 70 L1200 110 C700 50 300 70 0 170 Z" fill="#8a6cc0" opacity=".85"/>
  <path d="M0 150 C320 60 720 50 1200 100 L1200 115 C720 70 320 80 0 170 Z" fill="#ffffff" opacity=".7"/>
</svg>

<h1 class="section-title" style="top:790px">Welcome to Willow 4</h1>
<p class="intro" style="top:850px"><strong>Willow 4 is a free transgender and crossdressing support group committed to providing support and understanding to the transgender, crossdresser and gender diverse group including their partners, family and friends.</strong><br><br>
We are a small voluntary team who share our own stories, useful guides and trusted contacts. Whether you are just starting to ask questions or have been on your path for years, you are welcome here, and we hope you will find a kind word and the help you need.</p>

<div class="rule" style="top:990px"></div>

<h2 class="section-title" style="top:1020px">Our Mission</h2>
<div class="mission">
  <div class="mission-item">
    <svg width="56" height="44" viewBox="0 0 56 44"><circle cx="18" cy="12" r="8" fill="#6a4a9c"/><circle cx="38" cy="12" r="8" fill="#6a4a9c"/><path d="M4 42c0-12 28-12 28 0zM24 42c0-12 28-12 28 0z" fill="#6a4a9c"/></svg>
    To provide support and advice to the transgender community, friends and family alike
  </div>
  <div class="mission-item">
    <svg width="44" height="44" viewBox="0 0 44 44"><rect x="4" y="18" width="9" height="22" fill="#6a4a9c"/><path d="M16 40V18l10-14c4 0 5 3 4 7l-2 7h10c3 0 4 3 3 5l-4 15c-1 2-2 2-4 2z" fill="#6a4a9c"/></svg>
    To empower individuals with support and information to allow them to pursue their own true direction
  </div>
  <div class="mission-item">
    <svg width="44" height="44" viewBox="0 0 44 44"><circle cx="22" cy="22" r="20" fill="#6a4a9c"/><rect x="19.5" y="19" width="5" height="15" fill="#fff"/><circle cx="22" cy="12" r="3" fill="#fff"/></svg>
    To provide information and contacts already for transgender and crossdressers friendly services
  </div>
  <div class="mission-item">
    <svg width="52" height="44" viewBox="0 0 52 44"><path d="M26 6 50 18 26 30 2 18z" fill="#6a4a9c"/><path d="M12 24v10c8 6 20 6 28 0V24L26 31z" fill="#6a4a9c"/></svg>
    To provide education and awareness within the broader community
  </div>
  <div class="mission-item">
    <svg width="44" height="44" viewBox="0 0 44 44"><circle cx="22" cy="22" r="20" fill="#6a4a9c"/><path d="M22 22V2a20 20 0 0 1 20 20z" fill="#c9b8e6"/></svg>
    To hopefully lessen the unnecessary and avoidable stress within the transgender community
  </div>
</div>

<div class="rule" style="top:1260px"></div>

<h2 class="section-title" style="top:1275px">Recent News</h2>
<span class="arrow" style="left:100px">‹</span>
<span class="arrow" style="left:1082px">›</span>
<div class="news">
  <div class="news-card"><div class="news-photo" role="img" aria-label="News photo of a person in a bright costume at an event" style="background:linear-gradient(160deg,#2f3f5c,#7d8fb0 55%,#c9b9d8)"></div><p class="news-title">Aenean sollicitudin quam risus</p><p class="news-date">Jul 11, 2015</p></div>
  <div class="news-card"><div class="news-photo" role="img" aria-label="News photo of friends gathered at a community meeting" style="background:linear-gradient(160deg,#6d5a4e,#b8a08a 55%,#e5d6c7)"></div><p class="news-title">Aenean sollicitudin quam risus</p><p class="news-date">Jul 11, 2015</p></div>
  <div class="news-card"><div class="news-photo" role="img" aria-label="News photo from a colourful pride parade" style="background:linear-gradient(160deg,#4f6f3a,#c7a65a 50%,#e58fa0)"></div><p class="news-title">Aenean sollicitudin quam risus</p><p class="news-date">Jul 11, 2015</p></div>
  <div class="news-card"><div class="news-photo" role="img" aria-label="News photo of a parade participant in festive dress" style="background:linear-gradient(160deg,#5c6f2f,#c77a8c 55%,#e7c1a0)"></div><p class="news-title">Aenean sollicitudin quam risus</p><p class="news-date">Jul 11, 2015</p></div>
</div>

<section class="testimonial">
  <div class="quote-body">
    <div class="quote-mark">“</div>
    <p class="quote-text">Finding this group gave me the courage to speak openly with my family. The team listened without judgement, pointed me to a kind local doctor and checked in on me for weeks after. I no longer feel alone on this journey and I am so grateful for every chat and every friendly word along the way.</p>
    <p class="quote-name">Harper, OR</p>
  </div>
  <div class="quote-photo" role="img" aria-label="Portrait photo of a person with long hair seen from the side"></div>
</section>
<div class="dots"><span class="on"></span><span></span><span></span><span></span><span></span></div>

<h2 class="section-title" style="top:2055px">Contact us</h2>
<div class="contact-line">
  <span><svg width="14" height="14" viewBox="0 0 14 14"><path d="M3 1l3 3-2 2c1 2 2 3 4 4l2-2 3 3-2 2C6 13 1 8 1 3z" fill="#6a4a9c"/></svg>Call us : 0800 555 0144</span>
  <span><svg width="16" height="12" viewBox="0 0 16 12"><rect x="1" y="1" width="14" height="10" fill="none" stroke="#6a4a9c" stroke-width="1.5"/><path d="M1 1l7 6 7-6" fill="none" stroke="#6a4a9c" stroke-width="1.5"/></svg>E-mail : hello@willow4.org</span>
  <span><svg width="16" height="14" viewBox="0 0 16 14"><path d="M1 1h14v9H6l-4 3v-3H1z" fill="#6a4a9c"/></svg>Live Chat with us</span>
</div>

<footer class="footer">
  <p class="footer-links">Home &nbsp;|&nbsp; About us &nbsp;|&nbsp; Bios &nbsp;|&nbsp; News &nbsp;|&nbsp; Suggestions &nbsp;|&nbsp; Resources &nbsp;|&nbsp; Contact us</p>
  <p class="footer-copy">Copyright © 2015 Willow 4. All rights reserved.</p>
  <div class="social"><span></span><span></span><span></span><span></span><span></span></div>
</footer>
</body>
</html>
```